High Quality Business card for Property Management Agency - Super Classy and professional design

High Quality Business card design.

We need a business card designed for our Property Management Agency.
We are located on Sydney's Northern Beaches and manage beautiful properties along the beach and harbor.
We need a design that oozes modern, classy and professional.
I would like it to be double sided with contact details and logo on the front and just the logo on the back.

I need a print ready PDF version of the file as well as an editable photoshop (PSD) version of the file.

Logo and information details attached.

Target Market(s)

Property owners/investors, Male and Female Aged 28-65

Industry/Entity Type

Real Estate

Contact Information for Business Card

Tom Carrick
Tel: 0467 239 018
Email: tom@harvestlaneestates.com.au
Website: www.harvestlaneestates.com.au
Address: Level 2, 17 Wattlecourt Rd, Dunmarra NSW 2187

Font styles to use
Sans Serif

Requirements
Must have
• - Logo front and back
• - Business card details listed above and attached
• - Colour
Nice to have
• Sleek and professional

```html
<!DOCTYPE html>
<html lang="en">
<head>
<meta charset="utf-8">
<title>Harvest Lane Estates – Business Card</title>
<link href="https://fonts.googleapis.com/css2?family=Open+Sans:wght@300;400;700&display=swap" rel="stylesheet">
<style>
  :root {
    --stage: #d8d3cb;
    --paper: #f7f7f6;
    --charcoal: #2b2b2c;
    --ink: #2e2f31;
    --teal: #35a9b3;
    --teal-dark: #1f7f88;
    --rule: #474849;
    --light-text: #f1f1f1;
  }
  * { margin: 0; padding: 0; box-sizing: border-box; }
  html, body {
    width: 1200px; height: 892px; overflow: hidden;
    background: var(--stage);
    font-family: "Open Sans", sans-serif;
  }
  .stage {
    position: relative; width: 1200px; height: 892px;
    display: flex; flex-direction: column; align-items: center; justify-content: center; gap: 22px;
  }
  .card {
    position: relative; width: 680px; height: 415px;
    background: var(--paper);
    box-shadow: 0 6px 18px rgba(0,0,0,.18);
    overflow: hidden;
  }
  .brand {
    position: absolute; display: flex; align-items: center; gap: 10px;
    color: var(--ink); font-weight: 700; letter-spacing: .5px; white-space: nowrap;
  }
  .brand-mark { background: var(--teal); flex: none; }
  .front .brand { left: 34px; top: 56px; font-size: 20px; z-index: 1; }
  .front .brand-mark { width: 15px; height: 15px; }
  .back .brand { left: 50%; top: 50%; transform: translate(-50%, -50%); font-size: 40px; gap: 12px; }
  .back .brand-mark { width: 28px; height: 28px; }

  .details { position: absolute; inset: 0; }
  .row {
    position: absolute; right: 0;
    background: var(--charcoal);
    border-bottom: 1px solid var(--rule);
    display: flex; align-items: center;
    padding-left: 70px;
    color: var(--light-text);
  }
  .row:last-child { border-bottom: none; }
  .row-name    { top: 0;     height: 120px; left: 390px; }
  .row-online  { top: 120px; height: 95px;  left: 320px; }
  .row-phone   { top: 215px; height: 80px;  left: 260px; }
  .row-address { top: 295px; height: 120px; left: 200px; }
  .tab {
    position: absolute; left: -14px; top: 50%; transform: translateY(-50%);
    width: 46px; height: 42px; background: var(--teal);
    display: flex; align-items: center; justify-content: center;
  }
  .tab::before {
    content: ""; position: absolute; left: 0; bottom: -8px;
    border-top: 8px solid var(--teal-dark); border-left: 14px solid transparent;
  }
  .tab svg { width: 22px; height: 22px; }
  .person-name { font-size: 26px; font-weight: 300; letter-spacing: 1.5px; text-transform: uppercase; }
  .line { font-size: 15px; font-weight: 400; line-height: 1.45; }
</style>
</head>
<body>
<main class="stage">
  <section class="card front" aria-label="Card front">
    <div class="brand"><span class="brand-mark"></span>HARVEST LANE ESTATES</div>
    <div class="details">
      <div class="row row-name">
        <span class="tab"><svg viewBox="0 0 24 24" fill="#fff"><circle cx="12" cy="7.5" r="4.5"/><path d="M3 22c0-5 4-8.5 9-8.5s9 3.5 9 8.5z"/></svg></span>
        <span class="person-name">Tom Carrick</span>
      </div>
      <div class="row row-online">
        <span class="tab"><svg viewBox="0 0 24 24" fill="none" stroke="#fff" stroke-width="2"><circle cx="12" cy="12" r="4"/><path d="M16 8v5.5a2.5 2.5 0 0 0 5 0V12a9 9 0 1 0-3.5 7.1"/></svg></span>
        <div class="line">tom@harvestlaneestates.com.au<br>www.harvestlaneestates.com.au</div>
      </div>
      <div class="row row-phone">
        <span class="tab"><svg viewBox="0 0 24 24" fill="#fff"><path d="M6.6 10.8a15 15 0 0 0 6.6 6.6l2.2-2.2a1 1 0 0 1 1-.25 11.4 11.4 0 0 0 3.6.57 1 1 0 0 1 1 1V20a1 1 0 0 1-1 1A17 17 0 0 1 3 4a1 1 0 0 1 1-1h3.5a1 1 0 0 1 1 1c0 1.25.2 2.45.57 3.57a1 1 0 0 1-.25 1z"/></svg></span>
        <div class="line">0467 239 018</div>
      </div>
      <div class="row row-address">
        <span class="tab"><svg viewBox="0 0 24 24" fill="#fff"><path d="M12 3 2 12h3v9h5v-6h4v6h5v-9h3z"/></svg></span>
        <div class="line">Level 2, 17 Wattlecourt Rd, Dunmarra<br>NSW 2187</div>
      </div>
    </div>
  </section>

  <section class="card back" aria-label="Card back">
    <div class="brand"><span class="brand-mark"></span>HARVEST LANE ESTATES</div>
  </section>
</main>
</body>
</html>
```